Unique and original Business Card for Financial Services Business

I have moved premises and need to change the detail on my business card so thought now is a good time for a re-design. Looking for something professional and modern with colours to fit in with out logo. Like the idea of foil or embossing if that works but not a must have but I do want something that stands out and that I could not design myself.

Once business card is designed I will also be looking to get letterhead and flyers done but want the business card concept in place first.

The majority of designs I am receiving are generic and template based. I am looking for something unique and original. We have some great design elements in our logo, think outside the box and show me something that stands out from the crowd.

Target Market(s)

Business Professionals

Industry/Entity Type

Finance

Contact Information for Business Card

Name: Delia Norwood Phone 0473 958 162 Address PO Box 8617 Mossvale NSW 2389 Email info@steadyharbourfinancialservices.com.au website www.steadyharbourfinancialservices.com.au

Font styles to use
Other font styles liked:
• Ralway

Requirements
Should not have
• No black backgrounds please

```html
<!DOCTYPE html>
<html lang="en">
<head>
<meta charset="utf-8">
<title>Steady Harbour Financial Services – Business Card</title>
<link href="https://fonts.googleapis.com/css2?family=Raleway:wght@200;300;400;500&display=swap" rel="stylesheet">
<style>
  :root {
    --stage: #3b3b3b;
    --card-white: #ffffff;
    --ink: #3a3a3a;
    --teal: #13a195;
    --teal-bright: #11a99b;
    --teal-deep: #04535f;
    --navy: #022b44;
    --silver-light: #eeeeee;
    --silver-dark: #9a9a9a;
  }
  * { margin: 0; padding: 0; box-sizing: border-box; }
  html, body {
    width: 1200px;
    height: 800px;
    overflow: hidden;
    background: var(--stage);
    font-family: "Raleway", sans-serif;
  }
  .card {
    position: absolute;
    left: 315px;
    width: 571px;
    overflow: hidden;
  }
  .card-front {
    top: 51px;
    height: 329px;
    background: var(--card-white);
  }
  .card-back {
    top: 416px;
    height: 332px;
    background: linear-gradient(30deg, var(--teal-bright) 0%, var(--teal-deep) 60%, var(--navy) 100%);
  }
  .feature-area {
    position: absolute;
    top: 0;
    right: 0;
    width: 100px;
    height: 100%;
    background: linear-gradient(160deg, var(--silver-light) 0%, var(--silver-dark) 45%, var(--teal) 75%, var(--teal-deep) 100%);
  }
  .holder-name {
    position: absolute;
    left: 33px;
    top: 36px;
    font-size: 26px;
    font-weight: 500;
    color: var(--ink);
  }
  .holder-role {
    position: absolute;
    left: 33px;
    top: 70px;
    font-size: 17px;
    font-weight: 400;
    color: var(--teal);
  }
  .postal-address {
    position: absolute;
    left: 33px;
    top: 129px;
    font-size: 16.5px;
    line-height: 20px;
    color: var(--ink);
    font-style: normal;
  }
  .contact-list {
    position: absolute;
    left: 32px;
    top: 218px;
    list-style: none;
    font-size: 16px;
    color: var(--ink);
  }
  .contact-list li {
    display: flex;
    align-items: center;
    height: 27px;
    gap: 7px;
  }
  .contact-icon { width: 15px; height: 17px; flex: none; }
  .back-mark {
    position: absolute;
    left: 50%;
    top: 90px;
    transform: translateX(-50%);
    width: 92px;
    height: 92px;
    border: 3px solid var(--card-white);
    border-radius: 50%;
  }
  .company-name {
    position: absolute;
    left: 0;
    right: 0;
    top: 192px;
    text-align: center;
    color: var(--card-white);
    font-weight: 300;
  }
  .company-name .name-main {
    display: block;
    font-size: 42px;
    line-height: 46px;
    letter-spacing: -1px;
  }
  .company-name .name-sub {
    display: block;
    font-size: 20px;
    line-height: 24px;
    letter-spacing: 11px;
    margin-right: -11px;
  }
</style>
</head>
<body>

<section class="card card-front">
  <div class="feature-area" role="img" aria-label="Decorative brand artwork area in teal and silver"></div>

  <h1 class="holder-name">Delia Norwood</h1>
  <p class="holder-role">CEO, Founder</p>

  <address class="postal-address">
    PO Box 8617<br>
    Mossvale<br>
    NSW 2389
  </address>

  <ul class="contact-list">
    <li>
      <svg class="contact-icon" viewBox="0 0 14 16" aria-hidden="true">
        <rect x="3" y="0.8" width="8" height="14.4" rx="1.5" fill="none" stroke="#13a195" stroke-width="1.6"/>
        <circle cx="7" cy="12.8" r="0.9" fill="#13a195"/>
      </svg>
      <span>0473 958 162</span>
    </li>
    <li>
      <svg class="contact-icon" viewBox="0 0 14 16" aria-hidden="true">
        <rect x="0.5" y="4" width="13" height="9" fill="#13a195"/>
        <path d="M0.5 4 L7 9 L13.5 4" fill="none" stroke="#fff" stroke-width="1"/>
      </svg>
      <span>info@steadyharbourfinancialservices.com.au</span>
    </li>
    <li>
      <svg class="contact-icon" viewBox="0 0 14 16" aria-hidden="true">
        <g fill="none" stroke="#13a195" stroke-width="1.3">
          <circle cx="7" cy="8" r="6"/>
          <ellipse cx="7" cy="8" rx="2.6" ry="6"/>
          <path d="M1 8 H13 M2 5 H12 M2 11 H12"/>
        </g>
      </svg>
      <span>www.steadyharbourfinancialservices.com.au</span>
    </li>
  </ul>
</section>

<section class="card card-back">
  <div class="back-mark" aria-hidden="true"></div>
  <p class="company-name">
    <span class="name-main">STEADY HARBOUR</span>
    <span class="name-sub">Financial Services</span>
  </p>
</section>

</body>
</html>
```